Design some Business Cards (project 18 aug)

Please create a business card. You can find the logotype as attachment. The company core business is logotype design.
Size 90 x 55 mm. Please deliver in adobe Illustrator file format (.AI). Use dummy name and contact information.

```html
<!DOCTYPE html>
<html lang="en">
<head>
<meta charset="utf-8">
<title>Markcraft Business Card</title>
<link rel="stylesheet" href="https://fonts.googleapis.com/css2?family=Open+Sans:wght@400;600;700&display=swap">
<style>
  :root {
    --bg: #e9e5e0;
    --brand-blue: #3a52a3;
    --brand-red: #ed1c24;
    --brand-yellow: #f3ec19;
    --brand-green: #8dc63f;
    --rule: #d7e23a;
    --ink: #222222;
    --white: #ffffff;
    --silver: #e4e6ec;
  }
  * { margin: 0; padding: 0; box-sizing: border-box; }
  html, body { width: 1145px; height: 1200px; overflow: hidden; }
  body {
    background: var(--bg);
    font-family: "Open Sans", Arial, sans-serif;
    position: relative;
  }
  .card {
    position: absolute;
    left: 197px;
    width: 762px;
    height: 465px;
    border-radius: 26px;
    overflow: hidden;
  }
  .card--front { top: 92px; background: var(--brand-blue); }
  .card--back { top: 618px; background: var(--white); }

  .front-wordmark {
    position: absolute;
    top: 130px;
    left: 0;
    width: 100%;
    text-align: center;
    font-size: 72px;
    font-weight: 700;
    color: var(--silver);
    letter-spacing: 1px;
  }
  .front-url {
    position: absolute;
    top: 389px;
    left: 0;
    width: 100%;
    text-align: center;
    font-size: 15px;
    letter-spacing: 2.6px;
    color: var(--white);
  }
  .front-url .domain { color: var(--brand-red); }

  .back-wordmark {
    position: absolute;
    top: 50px;
    left: 38px;
    font-size: 30px;
    font-weight: 700;
    color: var(--brand-blue);
  }
  .holder-name {
    position: absolute;
    top: 141px;
    left: 38px;
    font-size: 33px;
    font-weight: 400;
    color: var(--brand-blue);
  }
  .holder-name .surname { color: var(--brand-red); }
  .holder-title {
    position: absolute;
    top: 189px;
    left: 38px;
    font-size: 15px;
    color: var(--brand-green);
  }
  .title-rule {
    position: absolute;
    top: 204px;
    left: 140px;
    width: 588px;
    height: 1.5px;
    background: var(--rule);
  }
  .contact-list {
    position: absolute;
    top: 338px;
    left: 36px;
    list-style: none;
  }
  .contact-list li {
    display: flex;
    align-items: center;
    height: 25px;
    font-size: 17px;
    color: var(--ink);
  }
  .contact-list svg { width: 19px; height: 19px; margin-right: 16px; flex: none; }
  .address {
    position: absolute;
    top: 338px;
    left: 483px;
    font-size: 16px;
    line-height: 25px;
    color: var(--ink);
    font-style: normal;
  }
  .footer-band {
    position: absolute;
    left: 0;
    bottom: 0;
    width: 100%;
    height: 36px;
  }
</style>
</head>
<body>

<section class="card card--front">
  <div class="front-wordmark">Markcraft</div>
  <div class="front-url">www.<span class="domain">alpinedeskservice</span>.com</div>
</section>

<section class="card card--back">
  <div class="back-wordmark">Markcraft</div>
  <h1 class="holder-name">Arjun <span class="surname">Mehta</span></h1>
  <div class="holder-title">CEO/Founder</div>
  <div class="title-rule"></div>

  <ul class="contact-list">
    <li>
      <svg viewBox="0 0 20 20" aria-hidden="true">
        <circle cx="10" cy="10" r="10" fill="var(--brand-blue)"/>
        <path d="M6.5 5.5l2 -0.5 1 2.5-1.2 1c.6 1.3 1.5 2.2 2.8 2.8l1-1.2 2.5 1-.5 2c-4 .3-7.9-3.6-7.6-7.6z" fill="#fff"/>
      </svg>
      48120-33574
    </li>
    <li>
      <svg viewBox="0 0 20 20" aria-hidden="true">
        <circle cx="10" cy="10" r="10" fill="var(--brand-yellow)"/>
        <path d="M6.5 5.5l2 -0.5 1 2.5-1.2 1c.6 1.3 1.5 2.2 2.8 2.8l1-1.2 2.5 1-.5 2c-4 .3-7.9-3.6-7.6-7.6z" fill="#8a8a8a"/>
      </svg>
      71604-28839
    </li>
    <li>
      <svg viewBox="0 0 20 20" aria-hidden="true">
        <circle cx="10" cy="10" r="10" fill="var(--brand-red)"/>
        <rect x="5" y="6.5" width="10" height="7" rx="1" fill="#fff"/>
        <path d="M5.5 7l4.5 3.5 4.5-3.5" fill="none" stroke="var(--brand-red)" stroke-width="1"/>
      </svg>
      arjun@markcraft.in
    </li>
  </ul>

  <address class="address">
    Alpine Desk Services GmbH<br>
    Lindenweg 14<br>
    CH-8400 Winterthur / Zurich
  </address>

  <svg class="footer-band" viewBox="0 0 762 36" preserveAspectRatio="none" aria-hidden="true">
    <rect x="0" y="0" width="762" height="36" fill="var(--brand-yellow)"/>
    <polygon points="386,0 762,0 762,36 373,36" fill="var(--white)"/>
    <polygon points="390,0 762,0 762,36 377,36" fill="var(--brand-red)"/>
  </svg>
</section>

</body>
</html>
```